Counseling Practice Business Card

I need a professional looking business card incorporating my new logo that was just completed. Card needs to incorporate my name and title, description of my specialty, my address, my phone number, my fax number, my email and my website URL. I need to be able to choose design on/with different paper colors and textures.
I do not have a lot of business card ideas so I am open to anything but I want bold,sharp, clear card without additional designs other than my logo (see attached file info). I am open to different color backgrounds or paper colors including black. I do not like traditional brackets around area codes in phone number or dashes between numbers in phone number. Am open to other ways of presenting including periods between numbers as appropriate. I do not know enough to know what I like yet but I want card to coordinate and work together with my logo. My practice emphasizes natural mental health interventions so any use of color (with background paper color or the blue and green in my logo) that elicits nature is nice. In addition to black, any natural brown or wood looking background might be desirable also. Most of the offerings so far look very similar and boring.

Target Market(s)

Potential therapy clients and other professionals

Contact Information for Business Card

Card information:
Marcus T. Whitfield, Ph.D.
Licensed Clinical Psychologist
Integrative Health Coach
4812 Ferndale Pkwy NW
Suite 730
Larkmont, GA 30218
(770) 555-0142 phone
(770) 555-0186 fax
drmarcuswhitfield@kelvora.com
pathbloomcounseling.com

Font styles to use
Serif
Sans Serif
Other font styles liked:
• anything that you think looks crisp, clear and easily readable

Requirements
Must have
• Any color used should coordinate with my logo design (see attached files).
• Card should be printed horizontally so top and bottom are longest sides of rectangle.
• Background color or paper color should complement and highlight logo. Do not like a white background. black, grey, brown or any color my logo would blend well with.
Nice to have
• I would like designer to utilize color to highlight letters/name or phone-fax-web symbols.
• Bottom edge of card could be highlighted if appropriate to an idea.
Should not have
• I would NOT want the card to have a pure white background at all.
• No clear cards.
• Cards should be oriented with long sides on bottom and top, NOT sides. DO NOT LIKE THIS THIN TALL ORIENTATION.

```html
<!DOCTYPE html>
<html lang="en">
<head>
<meta charset="utf-8">
<title>Pathbloom Counseling – Business Card</title>
<link href="https://fonts.googleapis.com/css2?family=Barlow:wght@400;500;600&display=swap" rel="stylesheet">
<style>
  :root{
    --green:#136a3c;
    --green-deep:#04552a;
    --blue:#00aeef;
    --brand-blue:#2a7cc7;
    --ink:#141515;
    --paper:#f8f8f8;
    --text-dark:#1d1d1d;
    --white:#ffffff;
  }
  *{margin:0;padding:0;box-sizing:border-box}
  html,body{width:1200px;height:1200px;overflow:hidden;background:var(--white);font-family:"Barlow",sans-serif}
  .card{position:absolute;left:180px;width:841px;height:480px;overflow:hidden}
  .card-front{top:84px;background:var(--ink)}
  .card-back{top:636px;left:178px;background:var(--paper)}

  .band{position:absolute;height:24px;width:50%}
  .band-top-left{top:0;left:0;background:var(--green)}
  .band-top-right{top:0;right:0;background:var(--blue)}
  .band-bottom-left{bottom:0;left:0;background:var(--blue)}
  .band-bottom-right{bottom:0;right:0;background:var(--green)}

  .map-backdrop{position:absolute;left:48px;top:48px;width:744px;height:380px;
    background:radial-gradient(ellipse at 50% 45%, #1b262b 0%, #171d20 55%, var(--ink) 100%);border-radius:40px}

  .brand{position:absolute;left:0;right:0;top:195px;text-align:center;color:var(--brand-blue);font-weight:600}
  .brand-name{font-size:68px;line-height:1;letter-spacing:1px}
  .brand-sub{font-size:24px;letter-spacing:15px;margin-top:6px;text-transform:uppercase;padding-left:15px}

  .back-art{position:absolute;inset:0}

  .identity{position:absolute;left:24px;top:196px;border-left:10px solid var(--green);padding-left:20px;height:88px}
  .person-name{position:absolute;left:30px;top:-10px;white-space:nowrap;font-size:32px;font-weight:600;color:var(--green);line-height:1.2}
  .person-name .first{display:inline-block;border-bottom:2px solid var(--blue);line-height:1}
  .person-title{position:absolute;left:30px;top:37px;white-space:nowrap;font-size:19px;color:var(--text-dark);line-height:24px}

  .contact-list{position:absolute;right:85px;top:0;list-style:none;color:var(--white);text-align:right;font-size:18.5px;font-weight:400}
  .contact-list li{position:absolute;right:0;white-space:nowrap;line-height:22px}

  .icon-strip{position:absolute;left:769px;top:116px;width:48px;height:244px;background:var(--green)}
  .icon-strip svg{position:absolute;left:0;top:0}
</style>
</head>
<body>

<section class="card card-front">
  <div class="band band-top-left"></div>
  <div class="band band-top-right"></div>
  <div class="map-backdrop" role="img" aria-label="Faint dotted world map backdrop"></div>
  <div class="brand">
    <div class="brand-name">Pathbloom</div>
    <div class="brand-sub">Counseling</div>
  </div>
  <div class="band band-bottom-left"></div>
  <div class="band band-bottom-right"></div>
</section>

<section class="card card-back">
  <svg class="back-art" width="841" height="480" viewBox="0 0 841 480">
    <polygon points="415,0 682,0 602,88" fill="var(--green)"/>
    <polygon points="682,0 580,76 602,88" fill="var(--green-deep)"/>
    <polygon points="682,0 841,0 841,480 258,480" fill="var(--blue)"/>
    <polygon points="274,112 335,128 290,174" fill="none" stroke="var(--blue)" stroke-width="3"/>
    <polygon points="292,326 387,304 362,398" fill="none" stroke="var(--green)" stroke-width="3"/>
    <path d="M70,366 q9,-11 18,0 t18,0 t18,0 t18,-2" fill="none" stroke="var(--blue)" stroke-width="3" stroke-linecap="round"/>
  </svg>

  <div class="identity">
    <h1 class="person-name"><span class="first">Marcus</span> T. Whitfield, Ph.D.</h1>
    <p class="person-title">Licensed Clinical Psychologist /<br>Integrative Health Coach</p>
  </div>

  <ul class="contact-list">
    <li style="top:143px">(770) 555-0142</li>
    <li style="top:182px">(770) 555-0186</li>
    <li style="top:221px">drmarcuswhitfield@kelvora.com</li>
    <li style="top:259px">pathbloomcounseling.com</li>
    <li style="top:294px">4812 Ferndale Pkwy NW<br>Suite 730, Larkmont, GA 30218</li>
  </ul>

  <div class="icon-strip">
    <svg width="48" height="244" viewBox="0 0 48 244" fill="var(--white)">
      <g stroke="#3f8a5e" stroke-width="1.5">
        <line x1="10" y1="57" x2="38" y2="57"/>
        <line x1="10" y1="96" x2="38" y2="96"/>
        <line x1="10" y1="135" x2="38" y2="135"/>
        <line x1="10" y1="174" x2="38" y2="174"/>
      </g>
      <path d="M19,38 c-2,-2 -2,-4 0,-6 l3,-2 c1,-1 2,-1 3,1 l2,3 c0,1 -1,2 -2,3 c2,3 4,5 7,7 c1,-1 2,-2 3,-2 l3,2 c2,1 2,2 1,3 l-2,3 c-2,2 -4,2 -6,0 c-5,-3 -9,-7 -12,-12 z" transform="translate(-3,-6)"/>
      <g transform="translate(14,74)">
        <rect x="0" y="4" width="4" height="14" rx="1"/>
        <rect x="5" y="6" width="15" height="12" rx="1"/>
        <rect x="8" y="0" width="9" height="5"/>
        <g fill="var(--green)"><rect x="8" y="9" width="2.5" height="2"/><rect x="12" y="9" width="2.5" height="2"/><rect x="16" y="9" width="2" height="2"/><rect x="8" y="13" width="2.5" height="2"/><rect x="12" y="13" width="2.5" height="2"/><rect x="16" y="13" width="2" height="2"/></g>
      </g>
      <g transform="translate(13,112)">
        <rect x="0" y="0" width="22" height="16" rx="2"/>
        <path d="M1,2 L11,9 L21,2" fill="none" stroke="var(--green)" stroke-width="2"/>
      </g>
      <g transform="translate(24,162)" fill="none" stroke="var(--white)" stroke-width="2">
        <circle r="10" fill="var(--white)"/>
        <g stroke="var(--green)" stroke-width="1.4">
          <ellipse rx="4.5" ry="10"/>
          <line x1="-10" y1="0" x2="10" y2="0"/>
          <line x1="0" y1="-10" x2="0" y2="10"/>
        </g>
      </g>
      <g transform="translate(12,190)">
        <path d="M0,12 L12,1 L24,12" fill="none" stroke="var(--white)" stroke-width="3" stroke-linejoin="round"/>
        <path d="M4,12 L12,5 L20,12 L20,22 L15,22 L15,16 L9,16 L9,22 L4,22 Z"/>
      </g>
    </svg>
  </div>
</section>

</body>
</html>
```